real estate agent looking for a business card

I am trying to brand myself and my team in the local real estate business. We just received new logo and we want to combine that with brandon Ashcroft logo.

I want my business card to look elegant, super sharp, and professional, but also, personable, because the brand is me myself.

About me; I sell only residential real estate, that is including single family homes, condominiums, vacant lands.

Reason: I am trying to get opinions of my team members about final logo selection.

Reason: During the holiday season, some of the members on vacation.

Target Market(s)

to consumers ages between 25-75

Industry/Entity Type

Real Estate Agent

Contact Information for Business Card

Name: Selin Odak-Branwell "Realtor"
Cell: (248) 555-0143
Direct Line: (248) 555-0187
Fax: (248) 555-0162
selinodak@maplenetmail.net
selin.bahomes.example

address: 41200 Pinecrest Parkway Suite:200
Alder Falls, OR 48990
Smaller font: Each office independently Owned and operated.
I want Brandon Ashcroft logo to be small and The Selin Group Logo to be visible.
My picture shall be on the right side
I prefer the background color to be black.

Font styles to use
Other font styles liked:
• i am flexible with font. i dont want script or decorative fonts though.

Requirements
Must have
• our tag line : Where Your Next Chapter Begins
Nice to have
• we want to look very sharp and elegant. something uniq looking business card.

```html
<!DOCTYPE html>
<html lang="en">
<head>
<meta charset="utf-8">
<title>The Selin Group – Business Card</title>
<link rel="stylesheet" href="https://fonts.googleapis.com/css2?family=Arimo:wght@400;700&display=swap">
<style>
  :root {
    --stage: #1c1c1c;
    --card: #ffffff;
    --gold: #c49a1c;
    --red: #c8102e;
    --ink: #1a1a1a;
    --grey: #8a8a8a;
    --photo-dark: #2b2b2b;
    --photo-light: #5a5a5a;
  }
  * { box-sizing: border-box; margin: 0; padding: 0; }
  html, body { width: 1200px; height: 750px; overflow: hidden; }
  body {
    background: var(--stage);
    font-family: "Arimo", Arial, sans-serif;
    color: var(--ink);
    display: flex;
    align-items: center;
    justify-content: center;
    gap: 40px;
  }
  .card {
    width: 540px;
    height: 309px;
    background: var(--card);
    position: relative;
    overflow: hidden;
  }

  /* Front */
  .card-front {
    display: flex;
    flex-direction: column;
    align-items: center;
    justify-content: center;
    padding-bottom: 40px;
  }
  .group-name {
    font-weight: 700;
    font-size: 44px;
    color: var(--gold);
    letter-spacing: 1px;
    line-height: 1;
  }
  .tagline {
    margin-top: 10px;
    font-size: 14px;
    font-weight: 700;
    color: var(--red);
    letter-spacing: 0.5px;
  }
  .front-web {
    position: absolute;
    bottom: 44px;
    left: 0;
    right: 0;
    text-align: center;
    font-size: 12px;
    letter-spacing: 4px;
    color: var(--ink);
  }

  /* Back */
  .card-back { display: flex; }
  .contact-panel {
    width: 46%;
    padding: 26px 0 0 24px;
  }
  .brokerage {
    font-size: 11px;
    color: var(--grey);
    letter-spacing: 0.5px;
  }
  .agent-name {
    margin-top: 14px;
    font-size: 19px;
    font-weight: 700;
    color: var(--gold);
  }
  .address {
    margin-top: 6px;
    font-size: 12.5px;
    line-height: 1.35;
  }
  .contact-list {
    list-style: none;
    margin-top: 10px;
    font-size: 12.5px;
    line-height: 1.5;
  }
  .contact-list li { display: flex; align-items: center; gap: 7px; white-space: nowrap; }
  .contact-list svg { width: 11px; height: 11px; fill: var(--gold); flex: none; }
  .photo {
    flex: 1;
    background: radial-gradient(ellipse at 55% 45%, var(--photo-light), var(--photo-dark) 75%);
  }
</style>
</head>
<body>
  <section class="card card-front">
    <div class="group-name">The Selin Group</div>
    <div class="tagline">Where Your Next Chapter Begins</div>
    <div class="front-web">www.selin.bahomes.example</div>
  </section>

  <section class="card card-back">
    <div class="contact-panel">
      <div class="brokerage">Brandon Ashcroft</div>
      <div class="agent-name">Selin Odak-Branwell</div>
      <div class="address">
        41200 Pinecrest Parkway<br>
        Suite:200<br>
        Alder Falls, OR 48990
      </div>
      <ul class="contact-list">
        <li><svg viewBox="0 0 12 12"><path d="M2 1h3l1 3-1.5 1a7 7 0 0 0 2.5 2.5L8 6l3 1v3a1 1 0 0 1-1 1A9 9 0 0 1 1 2a1 1 0 0 1 1-1z"/></svg>(248) 555-0187</li>
        <li><svg viewBox="0 0 12 12"><path d="M3 0h6a1 1 0 0 1 1 1v10a1 1 0 0 1-1 1H3a1 1 0 0 1-1-1V1a1 1 0 0 1 1-1zm0 2v7h6V2z"/></svg>(248) 555-0143</li>
        <li><svg viewBox="0 0 12 12"><path d="M3 0h5v4H3zM1 5h10v6H1zm2 2v1h2V7z"/></svg>(248) 555-0162</li>
        <li><svg viewBox="0 0 12 12"><path d="M0 2h12v8H0zm1 1v.5l5 3.5 5-3.5V3z"/></svg>selinodak@maplenetmail.net</li>
        <li><svg viewBox="0 0 12 12"><circle cx="6" cy="6" r="6"/></svg>www.selin.bahomes.example</li>
      </ul>
    </div>
    <div class="photo" role="img" aria-label="Portrait photograph of the agent in a dark blazer against a grey studio backdrop"></div>
  </section>
</body>
</html>
```